BRISKFIELD METRO ATHLETIDOME INVESTMENT BROCHURE*

We need an investment brochure for a new sportsplex being built to service the Greater Toronto Area. The attached file called "Brochure 2020" can be repurposed, with the Briskfield Metro Athletidome name and logo inserted wherever the Briskfield Metro Athletidome info currently exists.

We have also provided an excel file with 3 sheets-- each of these sheets is to be inserted into the brochure.

Target Market(s)

Investors

Logo Text

BRISKFIELD ATHLETIDOME

Requirements
Must have
• Project must reference:
The Worldwide trend to small sided soccer.

Investment opportunity that is eligible for registered funds (RRSPs and TFSAs)

Briskfield Metro Athletidome is a unique combination of sport and court that allows both players and spectators to be immersed with a fast-paced, high-energy game.
Should not have
• No wording or pages that reference "American" or USA.

```html
<!DOCTYPE html>
<html lang="en">
<head>
<meta charset="utf-8">
<title>Briskfield Metro Athletidome — Investment Brochure Spreads</title>
<link rel="stylesheet" href="https://fonts.googleapis.com/css2?family=Oswald:wght@300;400;500&family=Raleway:wght@200;300;400;600;700&display=swap">
<style>
:root{
  --gold:#d8c062;
  --gold-deep:#c7ad4c;
  --gold-soft:#e3d28a;
  --slate:#3f4459;
  --slate-deep:#353a4d;
  --navy:#2d3b82;
  --navy-deep:#24306b;
  --sky:#1ea8e6;
  --sky-soft:#59c2ef;
  --paper:#ffffff;
  --mist:#d9dce3;
  --ink:#3b3b3b;
  --muted:#8a8d96;
  --turf:#4d8a34;
  --turf-deep:#2f5e22;
  --head:"Oswald", "Arial Narrow", sans-serif;
  --body:"Raleway", "Helvetica Neue", sans-serif;
}
*{box-sizing:border-box;margin:0;padding:0}
html,body{width:1200px;height:1200px;overflow:hidden;background:var(--paper)}
.canvas{position:relative;width:1200px;height:1200px;overflow:hidden;background:var(--paper);font-family:var(--body);color:var(--ink)}
.spread{position:absolute;overflow:hidden;background:var(--paper);box-shadow:0 1px 4px rgba(0,0,0,.18)}
.abs{position:absolute}
.photo{position:absolute;background:linear-gradient(135deg,#6fa34e 0%,var(--turf) 45%,var(--turf-deep) 100%)}
.photo.dusk{background:linear-gradient(160deg,#2c3a2a 0%,#3f7a2f 55%,#8fd15a 100%)}
.photo.street{background:linear-gradient(160deg,#8e9aa3 0%,#b6b0a0 40%,#c9c2b0 100%)}
.photo.sky{background:linear-gradient(180deg,#c6d6e2 0%,#7fa06a 55%,#4b7b36 100%)}
.photo.indoor{background:linear-gradient(180deg,#cfd2d6 0%,#a5a9ae 50%,#8a2f2f 100%)}
.photo.dirt{background:linear-gradient(180deg,#c9cfd4 0%,#b39a7d 50%,#8d7458 100%)}
.gold-photo{position:absolute;left:0;top:0;background:linear-gradient(180deg,#d6c067 0%,#c9b257 45%,#b9a24a 100%)}
.frame{position:absolute;border:.6px solid rgba(255,255,255,.85)}
.tab{position:absolute;font-family:var(--head);font-weight:400;text-transform:uppercase;line-height:1;padding-left:9px;display:flex;flex-direction:column;justify-content:center}
.tab.gold{background:var(--gold);color:var(--paper);clip-path:polygon(0 0,100% 0,86% 100%,0 100%)}
.tab.dark{background:var(--slate);color:var(--paper);clip-path:polygon(0 0,100% 0,86% 100%,0 100%)}
.tab small{display:block;font-family:var(--body);font-style:italic;font-size:3.6px;text-transform:none;margin-top:1.5px;font-weight:400}
.tab.gold small{color:var(--slate)}
.tab.dark small{color:var(--gold)}
.intro-title{position:absolute;font-family:var(--head);font-weight:400;color:var(--paper);font-size:14.5px;line-height:.92;text-transform:uppercase;letter-spacing:-.1px}
.hex{clip-path:polygon(25% 0,75% 0,100% 50%,75% 100%,25% 100%,0 50%)}
.hex-pt{clip-path:polygon(50% 0,100% 25%,100% 75%,50% 100%,0 75%,0 25%)}

/* cover */
.cover-band{left:0;top:122px;width:261px;height:51px;background:linear-gradient(90deg,var(--navy-deep),var(--navy))}
.cover-mark{left:31px;top:88px;width:44px;height:44px;background:var(--navy)}
.cover-title{left:88px;top:123px;font-family:var(--head);font-size:17px;color:var(--paper);letter-spacing:-.2px}
.cover-sub{left:89px;top:143px;font-size:4.4px;letter-spacing:1.2px;color:var(--paper);font-weight:600;white-space:nowrap}
.cover-tag{left:89px;top:157px;font-size:2.6px;color:var(--paper);letter-spacing:.2px}

/* opportunity spread */
.brand-title{font-family:var(--head);color:var(--gold);font-size:8.6px;letter-spacing:-.1px;white-space:nowrap}
.brand-tag{font-size:3.2px;color:var(--muted);letter-spacing:.2px}
.body-copy{font-size:2.9px;line-height:1.5;color:var(--ink)}
.body-copy p+p{margin-top:3px}
.dark-copy{color:#c9ccd6}
.kicker{font-size:3.2px;color:var(--gold);font-weight:700;line-height:1.35}

/* revenue comparison */
.check-item{display:flex;align-items:center;gap:5px;font-size:3px;font-weight:600;color:var(--slate);line-height:1.3}
.check-item svg{flex:none}
.compare-panel{background:var(--mist)}
.compare-head{left:8px;top:6px;width:125px;height:18px;background:var(--gold);border-radius:0 9px 9px 9px;font-family:var(--head);font-size:4px;color:var(--paper);text-align:center}
.compare-head .right{position:absolute;right:0;top:0;width:56px;height:18px;background:var(--slate);border-radius:0 9px 0 9px;clip-path:polygon(12% 0,100% 0,100% 100%,0 100%);padding-top:4px;line-height:1.15}
.compare-head .left{position:absolute;left:0;top:4px;width:64px;line-height:1.15}
.compare-head .vs{position:absolute;left:60px;top:2px;font-size:9px;font-style:italic;color:var(--paper)}
.row-bar{position:absolute;left:6px;width:130px;height:10px;background:var(--sky);color:var(--paper);font-size:3.4px;display:flex;align-items:center;justify-content:space-between;padding:0 8px}
.row-bar .label{background:var(--sky-soft);padding:2px 10px;clip-path:polygon(6% 0,100% 0,94% 100%,0 100%);font-size:3.2px}
.row-bar.total{background:var(--slate)}
.row-bar.total .label{background:var(--gold)}

/* built to last */
.feature{position:absolute;display:flex;gap:4px;align-items:flex-start;color:var(--gold)}
.feature .ico{width:13px;height:13px;border:.7px solid var(--paper);border-radius:50%;flex:none}
.feature b{display:block;font-size:3.6px;font-weight:600;letter-spacing:.1px;line-height:1.1}
.feature span{display:block;font-size:2.4px;color:#c9ccd6;margin-top:1px}

/* projections table */
.proj{left:264px;top:11px;width:237px;font-size:2.1px;color:#222}
.proj-row{display:grid;grid-template-columns:34px 13px 18px 19px 20px 22px 21px 20px 20px 22px 28px;height:6.3px;align-items:center;border-bottom:.3px solid #b6b6b6}
.proj-row div{text-align:right;padding-right:1px;white-space:nowrap;overflow:hidden}
.proj-row div:first-child{text-align:left;padding-left:1px}
.proj-row.head{background:var(--mist);height:10px;font-weight:700}
.proj-row.head div{text-align:center;white-space:normal;line-height:1.1}
.proj-row.section div:first-child{background:#f4a21a;text-align:center}
.proj-row.section.green div:first-child{background:#8cc63f}
.proj-row.target{background:#a9d46a}
.roi{background:#fff;border:.3px solid #333;text-align:center !important;font-weight:700}
.roi.hot{background:#f3e23a}
.definitions{left:264px;top:136px;width:237px;height:38px;background:var(--gold);padding:3px 5px;font-size:2.4px}
.def-box{position:absolute;background:#fff;border:.3px solid #333;font-family:Georgia,serif;font-size:2.2px;line-height:1.5;padding:1px 2px}

/* benefits */
.pillar{position:absolute;top:96px;width:77px;height:72px;padding:7px 6px 0 8px}
.pillar h4{font-family:var(--body);font-weight:400;font-size:7px;line-height:.95;text-transform:uppercase;display:flex;gap:2px}
.pillar .num{width:7px;height:7px;border-radius:50%;background:var(--slate);color:var(--paper);font-size:4px;display:inline-flex;align-items:center;justify-content:center;flex:none;margin-top:1px}
.pillar p{font-size:2.4px;line-height:1.45;margin-top:9px}
.pillar.gold{background:var(--gold);color:var(--slate)}
.pillar.dark{background:var(--slate);color:var(--gold)}
.pillar.dark .num{background:var(--gold);color:var(--slate)}
.pillar.dark p{color:#c9ccd6}
.stat{position:absolute;width:54px;text-align:center;color:var(--paper)}
.stat .lab{font-size:2.8px;letter-spacing:.2px}
.stat .fig{position:relative;width:44px;height:40px;margin:7px auto 0}
.stat .fig span{position:absolute;inset:0;display:flex;align-items:center;justify-content:center;font-family:var(--head);font-size:17px;color:var(--gold);font-weight:300}
.stat .cap{font-size:2.1px;margin-top:5px;color:#c9ccd6}
.stat p{font-size:2.4px;line-height:1.45;color:#d4d6de;margin-top:10px;text-align:left;padding:0 4px}

/* less space diagram */
.node{position:absolute;width:56px;height:48px;background:var(--slate);color:var(--paper);font-size:3.6px;text-align:center;display:flex;align-items:center;justify-content:center;line-height:1.2;padding:0 8px}
.core{position:absolute;left:17px;top:52px;width:88px;height:76px;background:var(--gold);color:var(--paper);display:flex;flex-direction:column;align-items:center;justify-content:center;font-weight:700;font-size:6px;line-height:1.2;text-align:center}
.pill{position:absolute;left:304px;width:123px;height:29px;background:var(--slate);border-radius:0 15px 15px 0;padding:4px 0 0 14px;color:var(--paper)}
.pill b{display:block;font-size:4.6px;color:var(--gold);font-weight:600;letter-spacing:.2px}
.pill span{display:block;font-size:3px;line-height:1.35;margin-top:1px}
.grow{position:absolute;left:441px;top:33px;font-family:var(--body);font-weight:200;font-size:19.5px;line-height:.98;color:var(--gold);text-transform:uppercase;letter-spacing:-.4px}

/* product options */
.spec-list{position:absolute;font-size:3.3px;line-height:1.32;color:var(--gold)}
.spec-list li{list-style:none;position:relative;padding-left:5px}
.spec-list li::before{content:"";position:absolute;left:0;top:1.2px;width:1.6px;height:1.6px;border-radius:50%;background:var(--gold)}
.spec-list ul{margin-left:5px}
.spec-list ul li{color:var(--paper)}
.spec-list ul li::before{background:var(--paper)}
.spec-list .plain{padding-left:0}
.spec-list .plain::before{display:none}

/* pricing */
.tier{position:absolute;font-family:var(--body);font-size:5.2px;color:var(--paper);letter-spacing:.2px}
.price{position:absolute;width:30px;height:34px;display:flex;flex-direction:column;align-items:center;justify-content:center;line-height:1}
.price small{font-family:var(--head);font-size:3.8px;font-weight:300}
.price b{font-family:var(--body);font-size:7.6px;font-weight:600}
.price.good{background:var(--gold);color:var(--paper)}
.price.better{background:var(--paper);color:var(--slate)}
.price.best{background:var(--sky);color:var(--paper)}
.tier-note{position:absolute;left:147px;width:60px;font-size:2.3px;line-height:1.4;color:#d4d6de}
.tier-note b{display:block;font-weight:600;font-size:2.6px;color:var(--paper)}
</style>
</head>
<body>
<main class="canvas">

  <!-- Cover -->
  <section class="spread cover" style="left:113px;top:50px;width:261px;height:173px">
    <div class="photo" style="left:11px;top:0;width:239px;height:122px" role="img" aria-label="Aerial photo of a walled five-a-side turf field with players"></div>
    <div class="abs cover-band"></div>
    <div class="abs cover-mark"></div>
    <div class="abs cover-title">BEYOND THE TURF</div>
    <div class="abs cover-sub">BRISKFIELD METRO ATHLETIDOME</div>
    <div class="abs cover-tag">A REVOLUTIONARY SOCCER EXPERIENCE</div>
  </section>

  <!-- The Opportunity -->
  <section class="spread" style="left:113px;top:235px;width:529px;height:187px">
    <div class="abs" style="left:15px;top:22px;width:116px;height:126px;border:.7px solid var(--gold)"></div>
    <div class="photo" style="left:0;top:29px;width:143px;height:130px;clip-path:polygon(0 0,100% 0,86% 100%,0 100%)" role="img" aria-label="Photo of young players competing for the ball beside a sponsor wall"></div>
    <div class="abs brand-title" style="left:149px;top:39px">BRISKFIELD METRO ATHLETIDOME</div>
    <div class="abs brand-tag" style="left:149px;top:55px">SPORT | COMMUNITY | COURT</div>
    <div class="abs body-copy" style="left:139px;top:84px;width:110px">
      <p>At Briskfield Metro Athletidome, we know sport can change lives and transform communities. That's why we are committed to providing quality fields that are accessible, affordable and meaningfully local. Briskfield Metro Athletidome is a unique combination of sport and court that allows both players and spectators to be immersed with a fast-paced, high-energy game.</p>
      <p>Soccer is the beating heart of countless cultures around the world, yet local players have been held back too long by limited space. BMA helps remove these barriers by providing efficient, professional-grade fields that can be customized to nearly any space. Help us meet the demand for soccer in your neighbourhood and watch your community thrive. Join us today.</p>
    </div>

    <div class="abs" style="left:264px;top:0;width:265px;height:187px;background:var(--slate)"></div>
    <div class="tab gold" style="left:276px;top:11px;width:96px;height:25px;font-size:9px">The Opportunity<small>Entrepreneur</small></div>
    <div class="abs kicker" style="left:276px;top:46px;width:118px">AN INNOVATIVE INVESTMENT ELIGIBLE FOR REGISTERED FUNDS (RRSPs AND TFSAs)</div>
    <div class="abs body-copy dark-copy" style="left:276px;top:67px;width:124px">
      <p>The biggest soccer nations in the world are built on a futsal foundation. Elite players across the globe cite small-sided soccer as a decisive factor in their growth, and the worldwide trend to small-sided soccer keeps accelerating. Futsal is a game loved and played by people of all ages and backgrounds, and it fosters creativity and connection in every match.</p>
      <p>Across the Greater Toronto Area, the barriers to entry for quality playing fields are steep. Briskfield Metro Athletidome offers a high-quality, affordable solution that answers the need for field space and provides an environment for focused training and thrilling matches. Our fields can be installed on virtually any space: rooftops, gyms, tennis courts, lots. This investment opportunity is eligible for registered funds, including RRSPs and TFSAs. Join us in making this positive change in your neighbourhood.</p>
    </div>
    <div class="abs" style="left:406px;top:34px;width:100px;height:150px;border:.7px solid var(--gold)"></div>
    <div class="photo" style="left:410px;top:38px;width:100px;height:149px" role="img" aria-label="Photo of two players dribbling on a small indoor pitch"></div>
  </section>

  <!-- Benefits of five-a-side / Revenue comparison -->
  <section class="spread" style="left:113px;top:444px;width:525px;height:185px">
    <div class="gold-photo" style="width:262px;height:185px" role="img" aria-label="Gold-tinted photo of a stadium with turf fields"></div>
    <div class="frame" style="left:16px;top:16px;width:227px;height:154px"></div>
    <svg class="abs" style="left:0;top:0" width="262" height="185" viewBox="0 0 262 185"><polygon points="250,12 250,172 139,114" fill="var(--slate)"/></svg>
    <div class="intro-title" style="left:164px;top:100px">Benefits<br>of five-a-side</div>

    <div class="tab dark" style="left:273px;top:11px;width:96px;height:23px;font-size:8.5px">Revenue Comparison<small>ARENA SOCCER VS FIVE-A-SIDE</small></div>
    <svg class="abs" style="left:285px;top:36px" width="40" height="34" viewBox="0 0 40 34"><polygon points="0,0 40,0 0,34" fill="var(--gold)"/><text x="5" y="17" font-family="Oswald, sans-serif" font-size="14" fill="#fff">$</text></svg>
    <div class="abs" style="left:279px;top:80px;width:80px;display:flex;flex-direction:column;gap:13px">
      <div class="check-item"><svg width="8" height="8" viewBox="0 0 8 8"><circle cx="4" cy="4" r="4" fill="var(--slate)"/><path d="M2 4.2 3.5 5.6 6 2.6" stroke="var(--gold)" stroke-width=".9" fill="none"/></svg>MORE REVENUE PER SQUARE<br>FOOT = HAPPY OWNERS</div>
      <div class="check-item"><svg width="8" height="8" viewBox="0 0 8 8"><circle cx="4" cy="4" r="4" fill="var(--slate)"/><path d="M2 4.2 3.5 5.6 6 2.6" stroke="var(--gold)" stroke-width=".9" fill="none"/></svg>MORE PRIME TIME HOURS =<br>HAPPY CUSTOMERS</div>
      <div class="check-item"><svg width="8" height="8" viewBox="0 0 8 8"><circle cx="4" cy="4" r="4" fill="var(--slate)"/><path d="M2 4.2 3.5 5.6 6 2.6" stroke="var(--gold)" stroke-width=".9" fill="none"/></svg>DOUBLE YOUR PROGRAM<br>CAPACITY IN LESS SPACE</div>
    </div>
    <div class="abs compare-panel" style="left:372px;top:11px;width:141px;height:164px">
      <div class="abs compare-head">
        <div class="left">ARENA<br>SOCCER FIELD</div>
        <div class="vs">VS</div>
        <div class="right">FIVE - A- SIDE<br>PARK FIELD</div>
      </div>
      <div class="row-bar" style="top:36px"><span>16300SF</span><span class="label">SQUARE FOOTAGE</span><span>1400SF</span></div>
      <div class="row-bar" style="top:54px"><span>12</span><span class="label">PLAYER PER HOUR</span><span>20</span></div>
      <div class="row-bar" style="top:73px"><span>$10</span><span class="label">COST PER PLAYER PER HOUR</span><span>$10</span></div>
      <div class="row-bar" style="top:92px"><span>3000</span><span class="label">ANNUAL PRIME TIME HOUR</span><span>6000</span></div>
      <div class="row-bar" style="top:110px"><span>$21.18</span><span class="label">REVENUE PER SQUARE FOOT</span><span>$42.86</span></div>
      <div class="row-bar" style="top:129px"><span>$120</span><span class="label">REVENUE PER HOUR</span><span>$200</span></div>
      <div class="row-bar total" style="top:147px"><span>$360 000</span><span class="label">ANNUAL PRIME TIME REVENUE</span><span>$360 000</span></div>
    </div>
  </section>

  <!-- Products overview / Built to last -->
  <section class="spread" style="left:113px;top:657px;width:518px;height:185px">
    <div class="gold-photo" style="width:262px;height:185px" role="img" aria-label="Gold-tinted photo of a stadium with turf fields"></div>
    <div class="frame" style="left:16px;top:16px;width:227px;height:154px"></div>
    <svg class="abs" style="left:0;top:0" width="262" height="185" viewBox="0 0 262 185"><polygon points="251,12 251,174 139,120" fill="var(--slate)"/></svg>
    <div class="intro-title" style="left:164px;top:100px">Products<br>overview</div>

    <div class="abs" style="left:262px;top:0;width:256px;height:185px;background:var(--slate)"></div>
    <div class="photo" style="left:400px;top:0;width:118px;height:185px;-webkit-mask-image:linear-gradient(90deg,transparent,#000 35%);mask-image:linear-gradient(90deg,transparent,#000 35%)" role="img" aria-label="Aerial photo of a five-a-side field beside a park"></div>
    <div class="tab gold" style="left:267px;top:11px;width:96px;height:25px;font-size:9px">Built to last</div>
    <div class="feature" style="left:268px;top:50px;width:80px"><div class="ico"></div><div><b>COMMUNITY BUILDING</b><span>Inclusive. Accessible And Fun.</span></div></div>
    <div class="feature" style="left:346px;top:48px;width:80px"><div class="ico"></div><div><b>LONGITIVITY</b><span>Engineered for durability.</span></div></div>
    <div class="feature" style="left:268px;top:80px;width:80px"><div class="ico"></div><div><b>COMPATIBLE<br>CONSTRUCTION</b><span>Modularly designed for dense areas.</span></div></div>
    <div class="feature" style="left:346px;top:78px;width:80px"><div class="ico"></div><div><b>AFFORDABLE</b><span>Cheaper/more efficient than full fields.</span></div></div>
    <div class="feature" style="left:268px;top:110px;width:80px"><div class="ico"></div><div><b>SIMPLE SETUP</b><span>Installed in as little as 2-3 days.</span></div></div>
    <div class="feature" style="left:346px;top:108px;width:80px"><div class="ico"></div><div><b>KID FRIENDLY</b><span>Public use compliant. Tested for safety.</span></div></div>
    <div class="feature" style="left:268px;top:138px;width:80px"><div class="ico"></div><div><b>BRANDABLE</b><span>100% brandable wall panels.</span></div></div>
  </section>

  <!-- Revenue projections -->
  <section class="spread" style="left:113px;top:869px;width:512px;height:182px">
    <div class="gold-photo" style="width:258px;height:182px" role="img" aria-label="Gold-tinted photo of a stadium with turf fields"></div>
    <div class="frame" style="left:16px;top:15px;width:227px;height:154px"></div>
    <svg class="abs" style="left:0;top:0" width="258" height="182" viewBox="0 0 258 182"><polygon points="248,12 248,172 137,115" fill="var(--slate)"/></svg>
    <div class="intro-title" style="left:162px;top:97px">Revenue<br>projections</div>
    <div class="abs" style="left:17px;top:147px;width:150px;font-size:4px;line-height:1.2;color:var(--paper)">REVENUE PROJECTIONS: TWIN PAD INDOOR SOCCER PARK CENTRALLY LOCATED IN THE GTA</div>

    <div class="abs proj">
      <div class="proj-row head"><div>Scenario</div><div>Avg Hourly Rate</div><div>Weekly</div><div>Monthly</div><div>Annually</div><div>Total Expenses</div><div>Net Income</div><div>50% Investors</div><div>50% Mgmt Group</div><div>Investor ROI</div><div>Total ROI</div></div>
      <div class="proj-row section"><div>Conservative</div></div>
      <div class="proj-row"><div>Baseline (6 months full)</div><div>$140</div><div>7,700</div><div>33,367</div><div>400,400</div><div>351,700</div><div>48,700</div><div>24,350</div><div>24,350</div><div class="roi">5%</div><div class="roi">10%</div></div>
      <div class="proj-row"><div>Goal (8 months full)</div><div>$140</div><div>9,333</div><div>40,227</div><div>482,720</div><div>369,295</div><div>113,425</div><div>56,713</div><div>56,713</div><div class="roi">11%</div><div class="roi">22%</div></div>
      <div class="proj-row"><div>Stretch (10 months full)</div><div>$140</div><div>11,041</div><div>47,843</div><div>574,112</div><div>387,749</div><div>186,363</div><div>93,181</div><div>93,181</div><div class="roi">18%</div><div class="roi">36%</div></div>
      <div class="proj-row"><div>Full Capacity</div><div>$140</div><div>12,333</div><div>53,387</div><div>640,640</div><div>407,137</div><div>233,503</div><div>116,752</div><div>116,752</div><div class="roi">22%</div><div class="roi">45%</div></div>
      <div class="proj-row section green"><div>Target</div></div>
      <div class="proj-row target"><div>Baseline (6 months full)</div><div>$155</div><div>8,525</div><div>36,942</div><div>443,300</div><div>351,700</div><div>91,600</div><div>45,800</div><div>45,800</div><div class="roi">9%</div><div class="roi">18%</div></div>
      <div class="proj-row target"><div>Goal (8 months full)</div><div>$155</div><div>10,028</div><div>43,456</div><div>521,864</div><div>369,285</div><div>152,579</div><div>76,290</div><div>76,290</div><div class="roi hot">15%</div><div class="roi hot">30%</div></div>
      <div class="proj-row target"><div>Stretch (10 months full)</div><div>$155</div><div>12,224</div><div>52,970</div><div>635,624</div><div>387,749</div><div>247,875</div><div>123,938</div><div>123,938</div><div class="roi">24%</div><div class="roi">48%</div></div>
      <div class="proj-row target"><div>Full Capacity</div><div>$155</div><div>13,655</div><div>59,107</div><div>709,280</div><div>407,137</div><div>302,143</div><div>151,072</div><div>151,072</div><div class="roi">29%</div><div class="roi">58%</div></div>
      <div class="proj-row section"><div>Outperform</div></div>
      <div class="proj-row"><div>Baseline (6 months full)</div><div>$170</div><div>9,350</div><div>40,517</div><div>486,200</div><div>351,700</div><div>134,500</div><div>67,250</div><div>67,250</div><div class="roi">13%</div><div class="roi">26%</div></div>
      <div class="proj-row"><div>Goal (8 months full)</div><div>$170</div><div>10,807</div><div>46,831</div><div>561,968</div><div>369,285</div><div>192,683</div><div>96,342</div><div>96,342</div><div class="roi">19%</div><div class="roi">38%</div></div>
      <div class="proj-row"><div>Stretch (10 months full)</div><div>$170</div><div>13,406</div><div>58,096</div><div>697,136</div><div>387,749</div><div>309,387</div><div>154,693</div><div>154,693</div><div class="roi">30%</div><div class="roi">60%</div></div>
      <div class="proj-row"><div>Full Capacity</div><div>$170</div><div>14,966</div><div>64,827</div><div>777,920</div><div>407,137</div><div>370,783</div><div>185,392</div><div>185,392</div><div class="roi">36%</div><div class="roi">72%</div></div>
    </div>
    <div class="abs definitions">DEFINITIONS:
      <div class="def-box" style="left:5px;top:9px;width:112px">Full Capacity &nbsp;| Weekends and Holidays fully booked 8am to 10pm<br>&nbsp; &nbsp; &nbsp; &nbsp; &nbsp; &nbsp; &nbsp; &nbsp; &nbsp;| Weekdays fully booked 4pm to 10pm</div>
      <div class="def-box" style="left:122px;top:9px;width:110px">6 months full capacity | November 1st to April 30th<br>8 months full capacity | September 1st to April 30th<br>10 months full capacity | September 1st to June 30th</div>
    </div>
  </section>

  <!-- Benefits / Maximize your impact -->
  <section class="spread" style="left:652px;top:183px;width:505px;height:178px">
    <div class="photo sky" style="left:11px;top:11px;width:231px;height:85px" role="img" aria-label="Photo of a walled turf field with players beside a school building"></div>
    <div class="tab dark" style="left:11px;top:11px;width:90px;height:22px;font-size:8.5px">Benefits<small>Entrepreneur</small></div>
    <div class="pillar gold" style="left:11px"><h4><span class="num">1</span>Next gen of soccer business</h4><p>Tap into the booming worldwide trend to small-sided soccer. Be the first to give your town a thriving sports hub fit for all ages.</p></div>
    <div class="pillar dark" style="left:88px"><h4><span class="num">2</span>Smart &amp; sustaina-ble</h4><p>Generate strong return on investment with low-cost, high-value fields. More profit per square foot, branding options and low overhead.</p></div>
    <div class="pillar gold" style="left:165px"><h4><span class="num">3</span>Simple setup</h4><p>Speedy installation requires no pouring or foundation. Fields are modular, customizable and mobile, yet durable and built to last.</p></div>

    <div class="abs" style="left:242px;top:0;width:263px;height:178px;background:var(--gold)"></div>
    <svg class="abs" style="left:242px;top:0" width="263" height="178" viewBox="0 0 263 178"><polygon points="82,0 263,0 263,178 12,178" fill="var(--slate)"/></svg>
    <div class="tab gold" style="left:262px;top:12px;width:90px;height:19px;font-size:6.5px">Maximize your impact</div>
    <div class="stat" style="left:300px;top:44px"><div class="lab">SPACE EFFICIENCY</div><div class="fig"><svg width="44" height="40" viewBox="0 0 44 40"><polygon points="11,1 33,1 43,20 33,39 11,39 1,20" fill="none" stroke="var(--gold)" stroke-width=".7"/></svg><span>8X</span></div><div class="cap">MORE PLAYERS PER SQUARE FOOT</div><p>Walled courts coupled with the small-sided format are ideal for real estate constrained urban settings, fitting more kids per square foot.</p></div>
    <div class="stat" style="left:355px;top:44px"><div class="lab">PLAYER ENGAGEMENT</div><div class="fig"><svg width="44" height="40" viewBox="0 0 44 40"><polygon points="11,1 33,1 43,20 33,39 11,39 1,20" fill="none" stroke="var(--gold)" stroke-width=".7"/></svg><span>60%</span></div><div class="cap">MORE PLAYERS PER SQUARE FOOT</div><p>Our walled mini-pitches provide a continuous play environment that keeps every player involved and engaged at all times.</p></div>
    <div class="stat" style="left:410px;top:44px"><div class="lab">COMMUNITY ACTIVATION</div><div class="fig"><svg width="44" height="40" viewBox="0 0 44 40"><polygon points="11,1 33,1 43,20 33,39 11,39 1,20" fill="none" stroke="var(--gold)" stroke-width=".7"/></svg><span>100%</span></div><div class="cap">100% SPONSORSHIP POTENTIAL</div><p>BMA brings community together. High impact walls can be wrapped with sponsor messaging to offset project costs.</p></div>
  </section>

  <!-- Less space = more opportunity / Grow with intention -->
  <section class="spread" style="left:652px;top:392px;width:504px;height:178px">
    <div class="abs" style="left:11px;top:11px;width:229px;height:23px;background:var(--gold)"></div>
    <svg class="abs" style="left:11px;top:11px" width="229" height="23" viewBox="0 0 229 23"><polygon points="152,0 229,0 229,23 140,23" fill="var(--slate)"/></svg>
    <div class="abs" style="left:19px;top:15px;font-family:var(--head);font-size:7.5px;color:var(--paper)">LESS SPACE = MORE OPPORTUNITY</div>
    <div class="abs" style="left:19px;top:26px;font-size:2.4px;color:var(--paper)">HELPING YOU GROW YOUR BUSINESS</div>
    <svg class="abs" style="left:0;top:0" width="250" height="178" viewBox="0 0 250 178" fill="none" stroke="var(--slate)" stroke-width=".5">
      <polyline points="68,52 68,43 234,43 234,59 229,59"/>
      <polyline points="68,143 68,154 234,154 234,141 229,141"/>
      <line x1="106" y1="92" x2="111" y2="92"/>
      <polyline points="167,99 167,80 146,80"/>
      <line x1="196" y1="59" x2="184" y2="59"/>
      <line x1="196" y1="101" x2="184" y2="101"/>
    </svg>
    <div class="core hex"><svg width="16" height="16" viewBox="0 0 16 16"><rect x="0" y="0" width="16" height="16" rx="2" fill="var(--slate)"/><rect x="3.5" y="9" width="2" height="4" fill="var(--paper)"/><rect x="7" y="6" width="2" height="7" fill="var(--paper)"/><rect x="10.5" y="3" width="2" height="10" fill="var(--paper)"/></svg><div style="margin-top:4px">FIVE-A-SIDE<br>BENEFITS</div></div>
    <div class="node hex" style="left:111px;top:75px">LESS INVESTMENT</div>
    <div class="node hex" style="left:146px;top:53px">LESS SQUARE FOOTAGE REQUIRED</div>
    <div class="node hex" style="left:146px;top:96px">LESS SPACE BETWEEN PILLARS REQUIRED</div>
    <div class="node hex" style="left:183px;top:35px">MORE STARTUP CAPITAL</div>
    <div class="node hex" style="left:183px;top:77px">MORE AVAILABLE LOCATIONS</div>
    <div class="node hex" style="left:183px;top:117px">MORE FIELDS, MORE CUSTOMERS</div>

    <div class="abs" style="left:250px;top:0;width:133px;height:14px;background:var(--gold)"></div>
    <div class="abs" style="left:250px;top:0;width:54px;height:178px;background:var(--gold)"></div>
    <svg class="abs" style="left:250px;top:0" width="80" height="178" viewBox="0 0 80 178">
      <polygon points="20,52 34,38 48,52 40,52 40,158 28,158 28,52" fill="var(--slate)"/>
      <path d="M54 44 C54 28 64 16 78 16 L78 44 Z" fill="var(--gold)"/>
      <path d="M54 79 C54 63 64 51 78 51 L78 79 Z" fill="var(--gold)"/>
      <path d="M54 115 C54 99 64 87 78 87 L78 115 Z" fill="var(--gold)"/>
      <path d="M54 151 C54 135 64 122 78 122 L78 151 Z" fill="var(--gold)"/>
    </svg>
    <div class="pill" style="top:16px"><b>PERFORM</b><span>Enjoy Watching Players From Your Center<br>Achieve Greatness</span></div>
    <div class="pill" style="top:51px"><b>DEVELOP</b><span>Activate New Revenue Streams By Providing<br>Skills Programs</span></div>
    <div class="pill" style="top:87px"><b>FUFIL</b><span>Enjoy Watching Players From Your Center<br>Achieve Greatness</span></div>
    <div class="pill" style="top:122px"><b>CULTIVATE</b><span>Enjoy Watching Players From Your Center<br>Achieve Greatness</span></div>
    <div class="grow">Grow<br>with<br>inten-<br>tion</div>
    <div class="abs" style="left:441px;top:126px;font-size:3.6px;line-height:1.4;color:var(--muted)">MAKE AN IMPACT IN<br>YOUR COMMUNITY</div>
  </section>

  <!-- Skillcage option / Product specifications -->
  <section class="spread" style="left:652px;top:602px;width:509px;height:180px">
    <div class="photo street" style="left:0;top:0;width:142px;height:180px" role="img" aria-label="Photo of a child playing in a small walled cage beside a house"></div>
    <div class="abs" style="left:142px;top:0;width:226px;height:180px;background:var(--slate)"></div>
    <div class="photo dusk" style="left:368px;top:0;width:141px;height:180px" role="img" aria-label="Aerial night photo of a lit five-a-side field"></div>
    <div class="tab gold" style="left:142px;top:11px;width:96px;height:23px;font-size:8px">Skillcage option<small>Perfect for Smaller Areas, Indoor or Outdoor</small></div>
    <div class="tab gold" style="left:266px;top:12px;width:96px;height:25px;font-size:8px;line-height:1.05">Product<br>specifications</div>
    <ul class="spec-list" style="left:152px;top:50px;width:90px">
      <li>Standard Sizes<ul><li>20'x20' Footprint</li></ul></li>
      <li style="margin-top:3px">Standard Inclusions:<ul><li>Skillcage Goal: 3'x5'</li><li>Metal tubular goal netting</li><li>50" tall silver panel boards</li><li>Spectator handrails</li><li>11' total height containment netting</li><li>Step through door Environmental Turf (shown) or Pro Futsal Flooring</li></ul></li>
      <li>No foundations required</li>
      <li>Modular system allows for quick install and removal</li>
      <li>Customizing available</li>
      <li>Inquire for portable skill cage option</li>
      <li>Price: $8,200</li>
    </ul>
    <ul class="spec-list" style="left:266px;top:50px;width:96px">
      <li>Most Popular Layout:<ul><li>Field Playing Dimensions: (2) 50'x80'</li><li>Field Footprint: 53'x88'</li><li>Approx Park Footprint: 110'x130' (14,300 SF)</li></ul></li>
      <li style="margin-top:3px">Recommended Park Inclusions and Amenities
        <div style="color:var(--paper);padding-left:6px">Skillcage Goal: 3'x5'<br>Metal tubular goal netting<br>50" tall silver panel boards<br>Spectator handrails<br>11' total height containment netting<br>Step through door Environmental Turf (shown) or Pro Futsal Flooring</div></li>
      <li class="plain">No foundations required<br>Modular system allows for quick install and removal<br>Customizing available<br>Inquire for portable skill cage option</li>
    </ul>
  </section>

  <!-- Standard pricing / Warranty -->
  <section class="spread" style="left:652px;top:813px;width:502px;height:178px">
    <div class="gold-photo" style="width:502px;height:178px" role="img" aria-label="Gold-tinted photo of an outdoor field with containment netting"></div>
    <svg class="abs" style="left:0;top:0" width="502" height="178" viewBox="0 0 502 178">
      <polygon points="14,0 230,0 185,178 0,178 0,20" fill="var(--slate)"/>
      <polygon points="348,0 420,0 362,178 290,178" fill="var(--slate)"/>
    </svg>
    <div class="tab gold" style="left:154px;top:13px;width:70px;height:18px;font-size:6.5px">Standard pricing</div>
    <div class="tab gold" style="left:398px;top:13px;width:76px;height:18px;font-size:6.5px">Warranty &amp; lifespan</div>
    <div class="tier" style="left:32px;top:28px">GOOD:</div>
    <div class="price good hex-pt" style="left:26px;top:33px"><small>40'X60'</small><b>$52K</b></div>
    <div class="price good hex-pt" style="left:63px;top:33px"><small>50'X80'</small><b>$56K</b></div>
    <div class="price good hex-pt" style="left:104px;top:33px"><small>60'X100</small><b>$68K</b></div>
    <div class="tier" style="left:30px;top:70px">BETTER:</div>
    <div class="price better hex-pt" style="left:26px;top:77px"><small>40'X60'</small><b>$56K</b></div>
    <div class="price better hex-pt" style="left:63px;top:77px"><small>50'X80'</small><b>$94K</b></div>
    <div class="price better hex-pt" style="left:104px;top:77px"><small>60'X100</small><b>$166K</b></div>
    <div class="tier" style="left:35px;top:113px;color:var(--sky)">BEST:</div>
    <div class="price best hex-pt" style="left:26px;top:119px"><small>40'X60'</small><b>$52K</b></div>
    <div class="price best hex-pt" style="left:63px;top:119px"><small>50'X80'</small><b>$56K</b></div>
    <div class="price best hex-pt" style="left:104px;top:119px"><small>60'X100</small><b>$68K</b></div>
    <div class="tier-note" style="top:41px"><b>BEST</b>Walls, 2 Endline Goals, 2 Doors, Side &amp; Endline Netting, Turf Or Futsal Flooring, 4 Sideline Goals, Led Lights, Integrated Seating, Technology Package</div>
    <div class="tier-note" style="top:86px"><b>BETTER</b>Walls, 2 Endline Goals, 1 Door, Endline Netting, Turf Or Futsal Flooring</div>
    <div class="tier-note" style="top:126px"><b>GOOD</b>Walls, 2 Endline Goals, 1 Door</div>
  </section>

  <!-- Recent projects -->
  <section class="spread" style="left:652px;top:1003px;width:509px;height:178px">
    <div class="gold-photo" style="width:253px;height:178px" role="img" aria-label="Gold-tinted photo of a stadium with turf fields"></div>
    <div class="frame" style="left:16px;top:13px;width:227px;height:154px"></div>
    <svg class="abs" style="left:0;top:0" width="253" height="178" viewBox="0 0 253 178"><polygon points="242,9 242,165 132,109" fill="var(--slate)"/></svg>
    <div class="intro-title" style="left:160px;top:95px">Recent<br>projects</div>
    <div class="photo sky" style="left:264px;top:9px;width:76px;height:75px" role="img" aria-label="Photo of a completed outdoor five-a-side field"></div>
    <div class="photo dirt" style="left:343px;top:9px;width:76px;height:75px" role="img" aria-label="Photo of a field site under construction"></div>
    <div class="photo street" style="left:422px;top:9px;width:75px;height:75px" role="img" aria-label="Photo of a small cage installed in a backyard"></div>
    <div class="photo indoor" style="left:264px;top:89px;width:76px;height:75px" role="img" aria-label="Photo of an indoor field under ceiling lights"></div>
    <div class="photo sky" style="left:343px;top:89px;width:154px;height:75px" role="img" aria-label="Photo of an outdoor field surrounded by trees"></div>
  </section>

</main>
</body>
</html>
```